hi all

Im after a new age looking business card with my company logo on it

must include these details, I would like the PH and Email to be symbols

If the colours used for card could be kept within the colours used in logo that I have supplied that would be great, if another colour is to be used dark grey would be ok. no light bulbs etc thanks

Details below to be incorporated on card

Damian Holloway

Lic E871302

PH 0219647381

E info@brightvaleelectrical.example.nz

Domestic Commercial Industrial Electricians

```html
<!DOCTYPE html>
<html lang="en">
<head>
<meta charset="utf-8">
<title>Brightvale Electrical – Business Card</title>
<link rel="stylesheet" href="https://fonts.googleapis.com/css2?family=Jost:wght@300;400;600&display=swap">
<style>
  :root {
    --backdrop: #e9e6e1;
    --panel-white: #ecedee;
    --brand-blue: #2473ad;
    --brand-blue-dark: #1b5a89;
    --ink-dark: #2b2f33;
    --name-light: #d9dde1;
    --rule-light: #a9c6dc;
  }
  * { box-sizing: border-box; margin: 0; padding: 0; }
  html, body {
    width: 1200px; height: 693px; overflow: hidden;
    background: var(--backdrop);
    font-family: "Jost", sans-serif;
  }
  .card {
    position: absolute; left: 160px; top: 86px;
    width: 880px; height: 520px;
    display: flex;
    box-shadow: 0 10px 30px rgba(0,0,0,.18);
  }
  .card__brand {
    position: relative;
    width: 270px; height: 100%;
    background: var(--panel-white);
  }
  .card__details {
    position: relative;
    flex: 1; height: 100%;
    background: var(--brand-blue);
  }
  .logo {
    position: absolute; left: 42px; top: 168px;
    display: flex; align-items: center; gap: 10px;
  }
  .logo__dot {
    width: 30px; height: 30px; border-radius: 50%;
    background: var(--ink-dark);
    flex: none;
  }
  .logo__name {
    font-weight: 600; font-size: 24px; line-height: 1.05;
    color: var(--brand-blue);
    text-transform: uppercase; letter-spacing: .5px;
  }
  .circuit {
    position: absolute; left: 0; top: 380px;
    width: 270px; height: 20px;
  }
  .divider {
    position: absolute; left: 0; right: 0; top: 389px;
    height: 1px; background: var(--rule-light);
  }
  .holder {
    position: absolute; right: 70px; top: 200px;
    text-align: left;
  }
  .holder__name {
    font-weight: 300; font-size: 46px; letter-spacing: 1px;
    color: var(--name-light);
  }
  .holder__licence {
    margin-top: 4px;
    font-weight: 300; font-size: 17px; letter-spacing: 9px;
    color: var(--rule-light);
  }
  .contact {
    position: absolute; left: 40px; top: 300px;
    list-style: none;
    display: flex; flex-direction: column; gap: 10px;
  }
  .contact__item {
    display: flex; align-items: center; gap: 10px;
    font-weight: 300; font-size: 18px;
    color: var(--brand-blue-dark);
  }
  .contact__icon { width: 20px; height: 20px; flex: none; }
</style>
</head>
<body>
  <main class="card">
    <section class="card__brand">
      <div class="logo">
        <span class="logo__dot"></span>
        <span class="logo__name">Brightvale<br>Electrical</span>
      </div>
      <svg class="circuit" viewBox="0 0 270 20" aria-hidden="true">
        <line x1="0" y1="10" x2="146" y2="10" stroke="#2b2f33" stroke-width="1.2"/>
        <circle cx="150" cy="10" r="4" fill="none" stroke="#2b2f33" stroke-width="1.2"/>
        <circle cx="188" cy="10" r="4" fill="none" stroke="#2b2f33" stroke-width="1.2"/>
        <line x1="192" y1="10" x2="270" y2="10" stroke="#2b2f33" stroke-width="1.2"/>
      </svg>
    </section>
    <section class="card__details">
      <div class="holder">
        <p class="holder__name">Damian Holloway</p>
        <p class="holder__licence">Lic E871302</p>
      </div>
      <ul class="contact">
        <li class="contact__item">
          <svg class="contact__icon" viewBox="0 0 20 20" aria-label="Phone">
            <rect x="0" y="0" width="20" height="20" rx="4" fill="#1b5a89"/>
            <path d="M6 4.5c.6-.4 1.3-.3 1.6.3l1 1.8c.3.5.1 1.1-.3 1.4l-.7.5c.6 1.4 1.6 2.4 3 3l.5-.7c.3-.4.9-.6 1.4-.3l1.8 1c.6.3.7 1 .3 1.6l-.8 1c-.5.6-1.4.8-2.2.5C8.4 14.3 5.7 11.6 4.4 8.4c-.3-.8-.1-1.7.5-2.2z" fill="#2473ad"/>
          </svg>
          <span>0219647381</span>
        </li>
        <li class="contact__item">
          <svg class="contact__icon" viewBox="0 0 20 20" aria-label="Email">
            <rect x="1" y="4" width="18" height="12" rx="1" fill="none" stroke="#1b5a89" stroke-width="1.4"/>
            <path d="M1.5 4.8 10 11l8.5-6.2" fill="none" stroke="#1b5a89" stroke-width="1.4"/>
          </svg>
          <span>info@brightvaleelectrical.example.nz</span>
        </li>
      </ul>
    </section>
    <div class="divider"></div>
  </main>
</body>
</html>
```